依頼詳細
【デザイン改善要望】

・Klipora上のサムネイルのクリック率を上げたいで、インパクトのあるデザインをお願いします。

・Kliporaのサムネイルはやはり人(演者)の写真が入ったほうがインパクトが高いですが、このチャンネルはパペット人形をキャラクターにしているため、人に比べてインパクトが劣ります。そこをデザインの力でインパクトを出したいです。

・キャラクターは「写真」と「イラスト」のどちらも素材として添付しますので、デザインによって、どちらをお使い頂いても構いません。

・サムネイルでチャンネルの世界観を作りたいので、複数枚並んだ時に、全体として統一感が必要です。

【今後の継続依頼】

・今回のコンペで当選した場合、当選者の方にすべてのサムネイルの制作をお願いしたく思っております。

・当選後に別依頼として、50枚25,000円(コモリー受取額・税別)の金額条件にはお受け頂ける方を希望します。

・継続依頼を受けることができない、または、上記の条件では継続依頼を受けることができない方は、コンペへのご応募をお控え頂けますよう、お願い致します。
記載項目
動画キャッチコピー+キャラクター
サイズ
• 「横1280×縦720」×3つ
希望イメージ
シンプル 複雑
単色 カラフル
暗い 明るい
日常 高級
遊び心 厳粛
未来的 伝統的
女性的 男性的
希望する色
納品ファイル
• 高解像度JPG (.jpg)
• イラストレーター形式 (.ai)
• フォトショップ形式 (.psd)
• PNG形式 (.png)
補足説明
■ 選んだ理由

最もイメージに近いデザインをご提案頂き、誠にありがとうございました。また修正にも快く対応頂き、感謝しております。

■ 提案者全員のお礼・コメント

この度は当コンペにご参加頂き、誠にありがとうございました。たくさんの応募を頂き、どれも素晴らしいご提案で、とても選定が難しかったです。またの機会にぜひ宜しくお願い致します。

```html
<!DOCTYPE html>
<html lang="ja">
<head>
<meta charset="utf-8">
<title>サムネイル デザイン案</title>
<link href="https://fonts.googleapis.com/css2?family=M+PLUS+Rounded+1c:wght@800;900&family=Noto+Sans+JP:wght@500&display=swap" rel="stylesheet">
<style>
  :root {
    --page: #ffffff;
    --ink: #222222;
    --purple: #5b2d8e;
    --purple-deep: #3f1a6b;
    --navy: #1f2a78;
    --navy-deep: #141c55;
    --green: #1f6b2c;
    --green-deep: #124a1b;
    --yellow: #ffe100;
    --white: #ffffff;
    --outline: #1a1030;
    --char-light: #d9a25c;
    --char-dark: #8a5a2b;
  }
  * { box-sizing: border-box; margin: 0; padding: 0; }
  html, body { width: 849px; height: 1200px; overflow: hidden; background: var(--page); }
  .sheet { position: relative; width: 849px; height: 1200px; }
  .sheet-label {
    position: absolute; left: 161px; top: 50px;
    font: 500 15px "Noto Sans JP", sans-serif; color: var(--ink);
  }
  .thumb {
    position: absolute; left: 161px; width: 561px; height: 316px; overflow: hidden;
    font-family: "M PLUS Rounded 1c", sans-serif; font-weight: 900;
  }
  .thumb--intro { top: 90px; background: radial-gradient(circle at 70% 45%, var(--purple) 0%, var(--purple-deep) 100%); }
  .thumb--listen { top: 420px; background: radial-gradient(circle at 70% 45%, var(--navy) 0%, var(--navy-deep) 100%); }
  .thumb--persona { top: 750px; background: radial-gradient(circle at 70% 45%, var(--green) 0%, var(--green-deep) 100%); }
  .line {
    position: absolute; white-space: nowrap; line-height: 1;
    text-shadow:
      -3px -3px 0 var(--outline), 3px -3px 0 var(--outline), -3px 3px 0 var(--outline), 3px 3px 0 var(--outline),
      0 -3px 0 var(--outline), 0 3px 0 var(--outline), -3px 0 0 var(--outline), 3px 0 0 var(--outline),
      4px 5px 0 var(--outline);
  }
  .line--sub { color: var(--white); }
  .line--main { color: var(--yellow); }
  .small { font-size: 0.72em; }
  .character-art {
    position: absolute;
    background: radial-gradient(ellipse at 45% 40%, var(--char-light) 0%, var(--char-dark) 100%);
    border-radius: 45% 45% 40% 40%;
    opacity: 0.9;
  }
</style>
</head>
<body>
<main class="sheet">
  <p class="sheet-label">■デザイン案</p>

  <section class="thumb thumb--intro">
    <div class="character-art" role="img" aria-label="パペットのキャラクター2体のイラスト" style="left:330px; top:10px; width:200px; height:140px;"></div>
    <p class="line line--sub" style="left:42px; top:100px; font-size:38px;">1分で仕事<span class="small">も</span>人生<span class="small">も</span>変える</p>
    <h2 class="line line--main" style="left:40px; top:168px; font-size:86px;">自己紹介</h2>
  </section>

  <section class="thumb thumb--listen">
    <div class="character-art" role="img" aria-label="パペットのキャラクター2体のイラスト" style="left:365px; top:10px; width:170px; height:300px;"></div>
    <p class="line line--sub" style="left:30px; top:58px; font-size:42px;">会話<span class="small">が</span>上手<span class="small">くいく</span></p>
    <h2 class="line line--main" style="left:30px; top:118px; font-size:88px;">聞き上手</h2>
    <p class="line line--sub" style="left:32px; top:214px; font-size:31px;">3つのテクニック</p>
  </section>

  <section class="thumb thumb--persona">
    <div class="character-art" role="img" aria-label="パペットのキャラクター2体のイラスト" style="left:265px; top:140px; width:285px; height:190px;"></div>
    <p class="line line--sub" style="left:30px; top:24px; font-size:48px;">仕事<span class="small">が</span>上手<span class="small">くいく</span></p>
    <h2 class="line line--main" style="left:28px; top:104px; font-size:92px;">キャラ作り</h2>
  </section>
</main>
</body>
</html>
```